Talvex Industrial Maintenance Business Card

Design a business card with the following information, logo must be included.
Talvex Industrial Maintenance
Dale Virnow Jr.
Pone 413-627-8154
email dale.virnow.jr@brindlemail.net

```html
<!DOCTYPE html>
<html lang="en">
<head>
<meta charset="utf-8">
<title>Talvex Industrial Maintenance – Business Card</title>
<link rel="stylesheet" href="https://fonts.googleapis.com/css2?family=Montserrat:wght@400;500;700&display=swap">
<style>
  :root {
    --bg: #d4d4d2;
    --card-white: #ffffff;
    --brand-blue: #1a6fb8;
    --back-blue: #1473ba;
    --back-deep: #0f5c98;
    --back-soft: #2a82c4;
    --ink-grey: #555a60;
  }
  * { box-sizing: border-box; margin: 0; padding: 0; }
  html, body { width: 1200px; height: 801px; overflow: hidden; }
  body {
    background: var(--bg);
    font-family: "Montserrat", sans-serif;
    position: relative;
  }
  .card {
    position: absolute;
    left: 300px;
    width: 600px;
    height: 343px;
    box-shadow: 0 6px 18px rgba(0,0,0,.18);
  }
  .card-front { top: 36px; background: var(--card-white); border-bottom: 3px solid var(--brand-blue); }
  .card-back { top: 418px; background: var(--back-blue); overflow: hidden; }

  .front-layout {
    position: absolute; inset: 0;
    display: flex; align-items: center; justify-content: center; gap: 26px;
  }
  .brand { display: flex; align-items: center; gap: 12px; }
  .brand-dot { width: 34px; height: 34px; border-radius: 50%; background: var(--brand-blue); flex: none; }
  .brand-name {
    color: var(--brand-blue); font-weight: 700; font-size: 14px; line-height: 1.25;
    letter-spacing: .04em; text-transform: uppercase;
  }
  .divider { width: 1px; height: 92px; background: var(--brand-blue); }
  .contact { display: flex; flex-direction: column; gap: 9px; }
  .contact-name {
    color: var(--brand-blue); font-weight: 700; font-size: 17px;
    text-transform: uppercase; letter-spacing: .02em; margin-bottom: 3px;
  }
  .contact-line { display: flex; align-items: center; gap: 8px; color: var(--ink-grey); font-size: 12.5px; font-weight: 500; }
  .contact-line svg { width: 12px; height: 12px; fill: var(--brand-blue); flex: none; }

  .back-mark {
    position: absolute; left: 36px; top: 28px; width: 286px; height: 286px;
    border-radius: 50%;
    background: linear-gradient(135deg, var(--back-deep) 0%, var(--back-blue) 55%, var(--back-soft) 100%);
  }
  .back-name {
    position: absolute; right: 34px; bottom: 112px;
    color: var(--back-deep); font-weight: 700; font-size: 20px; line-height: 1.2;
    text-transform: uppercase; letter-spacing: .03em; text-align: left;
  }
</style>
</head>
<body>
  <section class="card card-front">
    <div class="front-layout">
      <div class="brand">
        <span class="brand-dot"></span>
        <p class="brand-name">Talvex<br>Industrial Maintenance</p>
      </div>
      <span class="divider"></span>
      <div class="contact">
        <p class="contact-name">Dale Virnow Jr.</p>
        <p class="contact-line">
          <svg viewBox="0 0 24 24" aria-hidden="true"><path d="M6.6 10.8a15.1 15.1 0 0 0 6.6 6.6l2.2-2.2a1 1 0 0 1 1-.25 11.4 11.4 0 0 0 3.6.57 1 1 0 0 1 1 1V20a1 1 0 0 1-1 1A17 17 0 0 1 3 4a1 1 0 0 1 1-1h3.5a1 1 0 0 1 1 1c0 1.25.2 2.46.57 3.6a1 1 0 0 1-.25 1z"/></svg>
          413-627-8154
        </p>
        <p class="contact-line">
          <svg viewBox="0 0 24 24" aria-hidden="true"><path d="M2 5h20v14H2zm2 2v.5l8 5 8-5V7zm0 3v7h16v-7l-8 5z"/></svg>
          dale.virnow.jr@brindlemail.net
        </p>
      </div>
    </div>
  </section>

  <section class="card card-back">
    <span class="back-mark"></span>
    <p class="back-name">Talvex<br>Industrial Maintenance</p>
  </section>
</body>
</html>
```